Gymnastics and fitness web design

Plavney Gymnastics and fitness centre is opening a new branch in the United States.
Target Audience:
22 to 40 year old people who are not satisfied with their current body figure, shape and size.
and
Our programs
Vexabolt, Sports performance and personal training
DESIGN STYLE:
We want the site to be trendy, edgy and cool. The colors we prefer are blue, black and silver. Th idea is people should get motivated by seeing our website. We don't like adding many text in the design, images oriented design is what we are after.
Contents should be added-
Slider
who we are?
section for our programs
Why us?
Video showing some tutorials
Articles
contact us form with map, Address, Phone number, timings, and social media buttons.

```html
<!DOCTYPE html>
<html lang="en">
<head>
<meta charset="utf-8">
<title>Plavney Fitness – Programs</title>
<link rel="stylesheet" href="https://fonts.googleapis.com/css2?family=Open+Sans:wght@400;600&display=swap">
<style>
:root{
  --navy:#323847;
  --blue:#2ea7dc;
  --ink:#333333;
  --muted:#9a9a9a;
  --white:#ffffff;
  --light:#f2f2f2;
  --icon:#3a3a3a;
}
*{box-sizing:border-box;margin:0;padding:0}
html,body{width:1200px;height:1108px;overflow:hidden}
body{font-family:"Open Sans",Arial,sans-serif;color:var(--ink);background:var(--white);position:relative}
section{position:absolute;left:0;width:1200px}
.section-title{position:absolute;left:0;width:1200px;text-align:center;font-size:26px;font-weight:600;line-height:1}
.section-title .accent{color:var(--blue)}
.title-rule{position:absolute;left:550px;width:100px;height:2px;background:var(--blue)}

.programs{top:0;height:428px;background:var(--navy)}
.programs .section-title{top:28px;color:var(--white)}
.programs .title-rule{top:63px}
.program-card{position:absolute;width:309px}
.program-photo{width:100%}
.program-label{background:var(--white);text-align:center;font-size:15px;color:var(--ink);display:flex;align-items:center;justify-content:center}
.program-label.active{background:var(--blue);color:var(--white);font-weight:600;font-size:14px}
.price-row{background:var(--white);height:41px;display:flex;align-items:center;justify-content:space-between;padding:0 9px}
.price{font-size:14px;color:var(--ink)}
.price .unit{color:var(--muted)}
.enroll{background:var(--blue);color:var(--white);font-size:11px;font-weight:600;padding:5px 8px;border-radius:2px}

.why-us{top:428px;height:251px;background:var(--white)}
.why-us .section-title{top:31px}
.why-us .title-rule{top:66px}
.feature{position:absolute;top:109px;width:200px;margin-left:-100px;text-align:center}
.feature svg{display:block;margin:0 auto;height:52px}
.feature-name{margin-top:18px;font-size:12px;color:var(--ink)}

.workouts{top:679px;height:429px;background:var(--light);border-bottom:2px solid var(--navy)}
.workouts .section-title{top:17px}
.workouts .title-rule{top:53px}
.workout{position:absolute;top:86px;width:306px}
.workout-media{position:relative;height:240px}
.play{position:absolute;left:50%;top:50%;width:50px;height:36px;margin:-18px 0 0 -25px;background:rgba(50,50,50,.85);border-radius:7px}
.play::after{content:"";position:absolute;left:20px;top:11px;border-left:13px solid var(--white);border-top:7px solid transparent;border-bottom:7px solid transparent}
.workout-meta{margin-top:5px;font-size:10.5px;color:var(--muted)}
.workout-title{margin-top:4px;font-size:12.5px;line-height:17px;color:var(--ink)}
</style>
</head>
<body>

<section class="programs">
  <h2 class="section-title">OUR <span class="accent">PROGRAMS</span></h2>
  <div class="title-rule"></div>

  <article class="program-card" style="left:111px;top:99px">
    <div class="program-photo" role="img" aria-label="Athlete flipping a large tyre in a gym" style="height:228px;background:linear-gradient(135deg,#3a3d40,#1c1e20 60%,#4a6b3a)"></div>
    <div class="program-label active" style="height:28px">VEXABOLT</div>
    <div class="price-row">
      <span class="price">$ 89.99/1 <span class="unit">Year</span></span>
      <span class="enroll">ENROLL NOW</span>
    </div>
  </article>

  <article class="program-card" style="left:446px;top:99px">
    <div class="program-photo" role="img" aria-label="Group doing agility drills on green turf" style="height:228px;background:linear-gradient(180deg,#8a8a86,#5e9a4e 55%,#3f8a3c)"></div>
    <div class="program-label" style="height:30px">SPORTS PERFORMANCE</div>
  </article>

  <article class="program-card" style="left:780px;top:101px">
    <div class="program-photo" role="img" aria-label="Trainer assisting a client with a dumbbell" style="height:225px;background:linear-gradient(135deg,#6f7880,#3a4450 55%,#243246)"></div>
    <div class="program-label" style="height:31px">PERSONAL TRAINING</div>
  </article>
</section>

<section class="why-us">
  <h2 class="section-title">WHY <span class="accent">US</span></h2>
  <div class="title-rule"></div>

  <div class="feature" style="left:349px">
    <svg viewBox="0 0 52 52" width="52" aria-hidden="true">
      <circle cx="26" cy="26" r="24" fill="none" stroke="var(--icon)" stroke-width="3"/>
      <rect x="11" y="19" width="5" height="14" rx="1.5" fill="var(--icon)"/>
      <rect x="17" y="16" width="5" height="20" rx="1.5" fill="var(--icon)"/>
      <rect x="30" y="16" width="5" height="20" rx="1.5" fill="var(--icon)"/>
      <rect x="36" y="19" width="5" height="14" rx="1.5" fill="var(--icon)"/>
      <rect x="22" y="24" width="8" height="4" fill="var(--icon)"/>
    </svg>
    <p class="feature-name">FITNESS EQUIPMENTS</p>
  </div>

  <div class="feature" style="left:602px">
    <svg viewBox="0 0 66 50" width="66" aria-hidden="true">
      <rect x="2" y="2" width="62" height="46" fill="none" stroke="var(--icon)" stroke-width="4"/>
      <circle cx="22" cy="19" r="6" fill="var(--icon)"/>
      <path d="M11 38c0-8 5-11 11-11s11 3 11 11z" fill="var(--icon)"/>
      <rect x="38" y="13" width="18" height="4" fill="var(--icon)"/>
      <rect x="38" y="22" width="18" height="4" fill="var(--icon)"/>
      <rect x="38" y="31" width="18" height="4" fill="var(--icon)"/>
    </svg>
    <p class="feature-name">2 YEARS MEMBERSHIP</p>
  </div>

  <div class="feature" style="left:850px">
    <svg viewBox="0 0 52 52" width="52" aria-hidden="true">
      <path d="M9 14A22 22 0 1 1 5 30" fill="none" stroke="var(--icon)" stroke-width="4"/>
      <path d="M3 6l2 14 13-4z" fill="var(--icon)"/>
      <path d="M26 13v15h11" fill="none" stroke="var(--icon)" stroke-width="4"/>
    </svg>
    <p class="feature-name">WE ARE OPEN 24 X 7</p>
  </div>
</section>

<section class="workouts">
  <h2 class="section-title">FEATURED <span class="accent">WORKOUTS</span></h2>
  <div class="title-rule"></div>

  <article class="workout" style="left:112px">
    <div class="workout-media" role="img" aria-label="Man sprinting against a concrete wall" style="background:linear-gradient(90deg,#b8c0c8,#8a929a 60%,#2e3236)"><span class="play"></span></div>
    <p class="workout-meta">Feb 19, 2017 · by Plavney</p>
    <h3 class="workout-title" style="font-weight:400">15 Min Better Posture Workout</h3>
  </article>

  <article class="workout" style="left:446px">
    <div class="workout-media" role="img" aria-label="Woman in sportswear doing cardio exercises" style="background:linear-gradient(90deg,#8c8c8c,#a6a6a6 55%,#c9c9c9)"><span class="play"></span></div>
    <p class="workout-meta">Feb 19, 2017 · by Plavney</p>
    <h3 class="workout-title" style="font-weight:400">10 Minute Workout : HIIT No Equipment Cardio Workout</h3>
  </article>

  <article class="workout" style="left:782px">
    <div class="workout-media" role="img" aria-label="Athlete lifting a barbell" style="background:linear-gradient(180deg,#f4f4f4,#d9a98a 45%,#3a3a3a)"><span class="play"></span></div>
    <p class="workout-meta">Feb 19, 2017 · by Plavney</p>
    <h3 class="workout-title" style="font-weight:400">5 Min Cool Down Exercises After Workout</h3>
  </article>
</section>

</body>
</html>
```